Lumo Vance IT company Soho london Stationary

We've just had a new logo designed on Gallow Pier and we now need some Stationary to go with it.
We're a small IT support firm supporting Design companies in Soho London. Most of our clients work on Vorls and a relatively creative so we want a relatively informal design on our stationary to reflect this.
We'd like to stick with the green in the logo but we're not adverse to adding another few colours to the palette.
Please see the attached file for our logo and not our website.

It Company

```html
<!DOCTYPE html>
<html lang="en">
<head>
<meta charset="utf-8">
<title>Lumo Vance – Business Cards</title>
<link rel="stylesheet" href="https://fonts.googleapis.com/css2?family=Source+Sans+3:wght@400;600;700&display=swap">
<style>
  :root {
    --backdrop: #2b2b2b;
    --card-white: #ffffff;
    --card-shade: #ececec;
    --lime: #a8d40a;
    --lime-deep: #78b41f;
    --ink: #111111;
    --muted: #5d6460;
    --pale: #e4e4e4;
  }
  * { margin: 0; padding: 0; box-sizing: border-box; }
  html, body { width: 900px; height: 1200px; overflow: hidden; }
  body {
    background: var(--backdrop);
    font-family: "Source Sans 3", "Myriad Pro", sans-serif;
    position: relative;
  }
  .card { position: absolute; overflow: hidden; }
  .card-front {
    left: 126px; top: 97px; width: 690px; height: 412px;
    background: linear-gradient(160deg, var(--card-white) 40%, var(--card-shade));
  }
  .card-back {
    left: 121px; top: 683px; width: 688px; height: 413px;
    background: var(--lime);
  }
  .decor { position: absolute; }
  .card-front .decor-top {
    left: 60px; top: 0; width: 300px; height: 150px;
    background: linear-gradient(180deg, var(--pale), rgba(228,228,228,0));
  }
  .card-front .decor-corner {
    left: 390px; top: 268px; width: 300px; height: 144px;
    background: linear-gradient(160deg, rgba(168,212,10,0) 20%, var(--lime));
  }
  .card-back .decor-sweep {
    left: 0; top: 0; width: 480px; height: 413px;
    background: linear-gradient(120deg, var(--lime-deep) 0%, rgba(120,180,31,0.35) 55%, rgba(120,180,31,0) 90%);
  }
  .brand {
    position: absolute;
    display: flex; align-items: center; gap: 10px;
    white-space: nowrap;
  }
  .card-front .brand {
    right: 26px; top: 34px;
    font-size: 44px; font-weight: 600; color: var(--lime);
  }
  .brand-dot {
    width: 14px; height: 14px; border-radius: 50%;
    background: currentColor;
  }
  .card-back .brand {
    left: 63px; top: 358px;
    font-size: 27px; font-weight: 700; color: var(--ink);
  }
  .holder {
    position: absolute; left: 55px; top: 172px;
    font-size: 35px; font-weight: 400; color: var(--ink); white-space: nowrap;
  }
  .holder .role {
    font-size: 24px; font-weight: 400;
    border-left: 2px solid var(--ink);
    padding-left: 6px; margin-left: 8px;
  }
  .contact {
    position: absolute;
    display: grid;
    grid-template-columns: 80px auto;
    column-gap: 12px;
    white-space: nowrap;
  }
  .card-front .contact {
    left: 56px; top: 258px;
    font-size: 23px; line-height: 37px; color: var(--muted);
  }
  .card-back .contact {
    left: 385px; top: 317px;
    font-size: 19px; line-height: 25.5px; color: var(--ink);
  }
  .address {
    position: absolute; left: 389px; top: 240px;
    font-size: 20px; font-weight: 700; line-height: 27px; color: var(--ink);
  }
</style>
</head>
<body>

<section class="card card-front" aria-label="Business card front">
  <div class="decor decor-top" role="img" aria-label="Pale grey sweeping leaf curves"></div>
  <div class="decor decor-corner" role="img" aria-label="Lime green and slate sweeping leaf curves"></div>
  <div class="brand"><span class="brand-name">Lumo Vance</span><span class="brand-dot"></span></div>
  <h1 class="holder">Tobin Marsh<span class="role">Web designer</span></h1>
  <div class="contact">
    <span>Phone</span><span>: 0207 555 0193</span>
    <span>E mail</span><span>: hello@lumo-vance.it</span>
    <span>Web</span><span>: www.lumo-vance.it</span>
  </div>
</section>

<section class="card card-back" aria-label="Business card back">
  <div class="decor decor-sweep" role="img" aria-label="Deep green sweeping leaf curves"></div>
  <p class="address">42 Larkin Row<br>London W1X 9ZQ.</p>
  <div class="contact">
    <span>Phone</span><span>: 0207 555 0193</span>
    <span>E mail</span><span>: hello@lumo-vance.it</span>
    <span>Web</span><span>: www.lumo-vance.it</span>
  </div>
  <div class="brand"><span class="brand-name">Lumo Vance</span><span class="brand-dot"></span></div>
</section>

</body>
</html>
```